I would like to modify/update my 2 step login screen

I want a more modern looking login page for our document imaging application. I need to keep all of the same elements and buttons that currently exist. The first 2 screens are the login. The 3rd is a screenshot of the actual application home page.

```html
<!DOCTYPE html>
<html lang="en">
<head>
<meta charset="utf-8">
<title>KRG Login Screens</title>
<link href="https://fonts.googleapis.com/css2?family=Inter:wght@400;500;600&display=swap" rel="stylesheet">
<style>
  :root {
    --canvas: #cccccc;
    --brand-red: #993a3c;
    --brand-red-dark: #7f2e31;
    --panel: #ececec;
    --field: #ffffff;
    --icon-cell: #dcdcdc;
    --ink: #333333;
    --muted: #9a9a9a;
    --green: #67b346;
    --green-dark: #4e8f33;
    --link: #3b82f6;
  }
  * { box-sizing: border-box; margin: 0; padding: 0; }
  html, body { width: 1041px; height: 1200px; overflow: hidden; }
  body { background: var(--canvas); font-family: "Inter", sans-serif; color: var(--ink); position: relative; }

  .screen { position: absolute; left: 130px; width: 781px; height: 390px; display: flex; box-shadow: 0 3px 10px rgba(0,0,0,.12); }
  .screen--classic { top: 127px; }
  .screen--sso { top: 667px; }

  .brand-side { position: relative; width: 390px; height: 100%; background: var(--brand-red); }
  .brand-visual { position: absolute; left: 38px; top: 63px; width: 309px; height: 208px; border-radius: 6px;
    background: linear-gradient(180deg, #d9e6f2 0%, #b9cde0 78%, #cfd2d6 82%, #aeb2b6 100%); }
  .brand-name { position: absolute; left: 0; right: 0; top: 318px; display: flex; align-items: center; justify-content: center; gap: 7px;
    color: #ffffff; font-weight: 600; font-size: 12px; letter-spacing: .5px; }
  .brand-name .dot { width: 14px; height: 14px; border-radius: 50%; background: #ffffff; }

  .form-side { position: relative; width: 391px; height: 100%; background: var(--panel); }
  .title { position: absolute; left: 0; right: 0; text-align: center; font-size: 12.5px; font-weight: 500; }

  .field, .btn { position: absolute; width: 233px; height: 28px; display: flex; border-radius: 3px; overflow: hidden; }
  .field .ico, .btn .ico { width: 28px; height: 28px; display: flex; align-items: center; justify-content: center; background: var(--icon-cell); flex: none; }
  .field .input { flex: 1; background: var(--field); font-size: 8.5px; color: #c4c4c4; display: flex; align-items: center; padding-left: 16px; }
  .field .input.center { justify-content: center; padding-left: 0; }
  .btn .label { flex: 1; display: flex; align-items: center; justify-content: center; font-size: 8.5px; font-weight: 500; background: var(--field); }
  .btn--green .label { background: var(--green); color: #ffffff; }
  .btn--green .ico { background: var(--green-dark); }
  .btn--solo .label { background: var(--green); color: #fff; }

  .options { position: absolute; left: 74px; width: 233px; display: flex; justify-content: space-between; align-items: center; font-size: 8.5px; }
  .options .remember { display: flex; align-items: center; gap: 6px; }
  .checkbox { width: 10px; height: 10px; border: 1px solid #666; border-radius: 2px; background: #fff; }
  .signup { position: absolute; left: 0; right: 0; text-align: center; font-size: 10px; }
  .signup a { color: var(--link); font-weight: 500; text-decoration: none; }
  .footer-links { position: absolute; font-size: 8.5px; }
  .footer-links span { color: #777; }
  .copyright { position: absolute; font-size: 6.5px; }
  .divider { position: absolute; left: 139px; width: 113px; display: flex; align-items: center; gap: 10px; font-size: 11px; color: #555; }
  .divider::before, .divider::after { content: ""; flex: 1; height: 1px; background: #d4d4d4; }
  .notice { position: absolute; left: 0; right: 0; text-align: center; font-size: 7.5px; line-height: 11px; color: #444; }
  .ico svg { display: block; }
</style>
</head>
<body>

<section class="screen screen--classic">
  <div class="brand-side">
    <div class="brand-visual" role="img" aria-label="Laptop showing the record management website home page"></div>
    <div class="brand-name"><span class="dot"></span>KEYSTONE RECORDS</div>
  </div>
  <div class="form-side">
    <h1 class="title" style="top:66px">CLASSIC Login</h1>
    <div class="field" style="left:74px;top:123px">
      <div class="ico"><svg width="13" height="13" viewBox="0 0 16 16" fill="none" stroke="#444" stroke-width="1.5"><circle cx="8" cy="5" r="3"/><path d="M2 15v-2a4 4 0 0 1 4-4h4a4 4 0 0 1 4 4v2z"/></svg></div>
      <div class="input">Enter Username Here</div>
    </div>
    <div class="field" style="left:74px;top:163px">
      <div class="ico"><svg width="16" height="10" viewBox="0 0 20 12" fill="none" stroke="#444" stroke-width="1.5"><circle cx="5" cy="6" r="4"/><circle cx="5" cy="6" r="1.3"/><path d="M9 6h10M15 6v3M18 6v2"/></svg></div>
      <div class="input">Enter Password Here</div>
    </div>
    <div class="btn btn--solo" style="left:74px;top:203px"><div class="label">Log in to KRG Demo23</div></div>
    <div class="options" style="top:244px">
      <div class="remember"><span class="checkbox"></span>Remember me</div>
      <div>Forgot Password?</div>
    </div>
    <p class="signup" style="top:288px">Don't have an account? <a href="#">Sign Up</a></p>
    <p class="footer-links" style="top:345px;left:0;right:0;text-align:center">Privacy <span>|</span> Remote support <span>|</span> Contact Us</p>
    <p class="copyright" style="top:362px;left:0;right:0;text-align:center">Copyright 2007-2024 Keystone Records Group</p>
  </div>
</section>

<section class="screen screen--sso">
  <div class="brand-side">
    <div class="brand-visual" role="img" aria-label="Laptop showing the record management website home page"></div>
    <div class="brand-name"><span class="dot"></span>KEYSTONE RECORDS</div>
  </div>
  <div class="form-side">
    <h1 class="title" style="top:54px">KRG Login</h1>
    <div class="field" style="left:79px;top:100px">
      <div class="ico"><svg width="12" height="13" viewBox="0 0 14 16" fill="#444"><ellipse cx="7" cy="3" rx="6" ry="2.5"/><path d="M1 5.5c0 1.4 2.7 2.5 6 2.5s6-1.1 6-2.5V8c0 1.4-2.7 2.5-6 2.5S1 9.4 1 8z"/><path d="M1 10.5c0 1.4 2.7 2.5 6 2.5s6-1.1 6-2.5V13c0 1.4-2.7 2.5-6 2.5S1 14.4 1 13z"/></svg></div>
      <div class="input center">Database Name</div>
    </div>
    <div class="btn btn--green" style="left:79px;top:137px">
      <div class="ico"><svg width="13" height="12" viewBox="0 0 16 14" fill="none" stroke="#fff" stroke-width="1.5"><rect x="1" y="1" width="14" height="10" rx="1"/><circle cx="8" cy="5" r="1.6"/><path d="M5 10a3 3 0 0 1 6 0M5 13h6"/></svg></div>
      <div class="label">Log in with myKRView</div>
    </div>
    <div class="divider" style="top:171px">or</div>
    <div class="btn" style="left:79px;top:193px">
      <div class="ico"><svg width="12" height="12"><circle cx="6" cy="6" r="5.5" fill="#444"/></svg></div>
      <div class="label">Continue with Northmail</div>
    </div>
    <div class="btn" style="left:79px;top:229px">
      <div class="ico"><svg width="12" height="12"><rect width="12" height="12" fill="#444"/></svg></div>
      <div class="label">Continue with Bluegate</div>
    </div>
    <div class="btn" style="left:79px;top:265px">
      <div class="ico"><svg width="12" height="12"><circle cx="6" cy="6" r="5.5" fill="#222"/></svg></div>
      <div class="label">Continue with KeyPass</div>
    </div>
    <p class="notice" style="top:316px">All activity on this site is being recorded.<br>Your IP Address is being saved as '192.168.168.134'.</p>
    <p class="footer-links" style="top:368px;left:26px;font-size:6.5px">Privacy <span>|</span> Remote support <span>|</span> Contact Us</p>
    <p class="copyright" style="top:369px;right:23px">Copyright 2007-2024 Keystone Records Group</p>
  </div>
</section>

</body>
</html>
```